Need 8.5" x 11" as well as large 11"x17" Posters for our upcoming event

Please include LOGOs in poster
Main logo is Harborview Teen Circle of PL

All high school age faith groups are invited to come and join with 150 to 175 other high school students from various faith traditions to participate in the Harborview Teen Circle of Pine Lakes‘s Annual Kindred Voices Gathering. More than ever, our county and world need young leaders who are willing to learn from each other and build stronger communities!

KINDRED GATHERING
The purpose of this Interfaith Youth Forum is to bring together young people from diverse ethnic, cultural, and religious backgrounds, and to engage them in dialogue. True dialogue is a conversation on a common subject between two or more persons of differing points of view and/or backgrounds. We feel that this commitment to dialogue will affect relationships in a constructive way in our places of worship and in our community.
The forum itself involves having eight religiously diverse high school-age students, one adult, and youth leader around each table to discuss common questions. Our youth leaders act as facilitators, but it is stressed that it is the students we want to hear from.
RSVP for our KINDRED GATHERING before February 18th, 2018
FORUM QUESTIONS Available online at http://htcpl-example.org/home/kindred-fair/

Target Market(s)

Houses of worship, community leaders, High School Students

Industry/Entity Type

Non-Profit

Font styles to use
Serif

Colors
cfdeed
0255a3
f78f20
f37122
f68d4d
faa54b
ffcf3e
ffc214
34a6d7

Requirements
Must have
• Harborview Teen Circle of Pine Lakes's 14th Annual Kindred Gathering & Fair
• TEENS EXPRESSING THEIR FAITH THROUGH ART, MUSIC, AND DIALOGUE
• THIS YEAR'S THEME: “Who Are You?”
• Sunday, March 11th, 2018 11:00am-5:00pm
• Congregation Ner Adamah
• 4187 W Larkmont Rd. Santa Ana, CA 92705
• Email: htcplorg@mailbox-example.com
• Website: HTCPL-example.org
• Facebook: Harborview Teen Circle of Pine Lakes
Nice to have
• Descriptions provided in word doc
Should not have
• -

```html
<!DOCTYPE html>
<html lang="en">
<head>
<meta charset="utf-8">
<title>Interfaith Youth Forum – Poster</title>
<link href="https://fonts.googleapis.com/css2?family=Crimson+Pro:wght@400;500&family=Tinos:wght@400&family=Raleway:wght@400&family=Oswald:wght@400;500;600&display=swap" rel="stylesheet">
<style>
  :root{
    --navy:#262e66;
    --navy-deep:#1f2758;
    --cream:#fdf7d6;
    --gold:#f6b930;
    --orange:#ef8a2a;
    --orange-text:#e5762a;
    --sky:#5bb8f0;
    --cyan:#49d0f4;
    --white:#ffffff;
    --page:#e9e9ec;
    --partner-green:#3f9a3c;
    --partner-brown:#c77a2e;
  }
  *{box-sizing:border-box;margin:0;padding:0}
  html,body{width:1200px;height:1200px;overflow:hidden;background:var(--page)}
  .poster{
    position:absolute;left:152px;top:17px;width:1018px;height:1324px;
    transform:scale(.88);transform-origin:top left;
    background:var(--navy);overflow:hidden;
    font-family:"Tinos",serif;color:var(--white);
  }
  .backdrop{position:absolute;inset:0}
  .abs{position:absolute}

  /* header */
  .org-seal{left:99px;top:40px;width:210px;height:210px;border:3px solid var(--navy);border-radius:50%;
    display:flex;align-items:center;justify-content:center;text-align:center;padding:24px;
    font-family:"Oswald",sans-serif;font-weight:500;font-size:24px;line-height:1.15;color:var(--navy)}
  .edition{left:344px;top:28px;font-family:"Crimson Pro",serif;font-size:26px;color:var(--orange-text)}
  .tagline{left:344px;top:70px;font-family:"Raleway",sans-serif;font-size:23px;line-height:35px;color:var(--navy)}
  .event-title{left:340px;top:136px;font-family:"Oswald",sans-serif;font-weight:600;font-size:60px;line-height:1;color:var(--navy);letter-spacing:-.5px;transform:scaleX(.97);transform-origin:left}
  .theme{left:344px;top:210px;font-family:"Crimson Pro",serif;font-size:26px;color:var(--navy)}
  .theme span{color:var(--orange-text)}

  /* intro */
  .intro{left:67px;top:418px;width:590px;font-size:14.6px;line-height:24.5px}
  .divider-v{width:1px;background:rgba(255,255,255,.8)}
  .when{left:692px;top:390px;width:281px;text-align:right;font-family:"Oswald",sans-serif;color:var(--gold);white-space:nowrap}
  .when .day{font-size:30px;font-weight:500}
  .when .day em{font-style:normal;font-size:23px;color:var(--white)}
  .when .time{font-size:21px;margin-top:-2px}
  .when .venue{font-size:29px;font-weight:500;line-height:1.2;letter-spacing:-.3px}
  .when .addr{font-size:13px;color:var(--gold)}
  sup{font-size:.55em}

  /* photo strip */
  .strip{left:66px;top:550px;width:905px;height:200px}
  .bars{display:flex;height:14px}
  .bars i{display:block;height:14px}
  .photos{display:flex;height:186px}
  .photos div{height:186px}

  /* sections */
  .sec-title{font-family:"Oswald",sans-serif;font-weight:600;line-height:1;letter-spacing:-.3px;white-space:nowrap}
  .gathering-title{left:69px;top:788px;width:240px;font-size:27px}
  .gathering-title span{color:var(--sky)}
  .rsvp{text-align:center;font-family:"Oswald",sans-serif}
  .rsvp small{display:block;font-size:11px;font-weight:400}
  .rsvp strong{display:block;font-size:21px;font-weight:400;color:var(--gold)}
  .gathering-rsvp{left:60px;top:848px;width:240px}
  .questions{left:56px;top:910px;width:248px;text-align:center;font-family:"Oswald",sans-serif}
  .questions small{display:block;font-size:11px}
  .questions a{font-size:11.5px;color:var(--gold);text-decoration:none}
  .questions b{font-weight:400;color:var(--white)}
  .gathering-photo{left:71px;top:959px;width:218px;height:163px}
  .purpose{left:332px;top:786px;width:626px;font-size:12.9px;line-height:15.2px}
  .purpose p+p{margin-top:15px}
  .purpose .clip{height:30px;overflow:hidden}
  .divider-h{left:332px;top:912px;width:626px;height:1px;background:rgba(255,255,255,.8)}
  .festival-title{left:331px;top:937px;font-size:44px}
  .festival-title span{color:var(--gold)}
  .festival-text{left:331px;top:1002px;width:252px;font-size:12.9px;line-height:15.2px}
  .festival-rsvp{left:386px;top:1142px;text-align:left}
  .festival-rsvp small{font-size:11px}
  .festival-rsvp strong{font-size:21px;line-height:28px}
  .festival-rsvp strong b{color:var(--white);font-weight:400}
  .gallery-title{left:652px;top:937px;font-size:44px}
  .gallery-title span{color:var(--orange)}
  .gallery-text{left:655px;top:992px;width:310px;font-size:12.9px;line-height:15.2px}
  .gallery-due{left:655px;top:1081px;font-family:"Oswald",sans-serif}
  .gallery-due small{display:block;font-size:11px}
  .gallery-due strong{display:block;font-size:21px;font-weight:400;color:var(--white)}
  .gallery-due strong span{color:var(--gold)}
  .contact-label{left:657px;top:1166px;font-family:"Oswald",sans-serif;font-size:12px;line-height:13px}
  .contact-list{left:742px;top:1163px;list-style:none;font-family:"Oswald",sans-serif;font-size:13px;color:var(--sky)}
  .contact-list li{display:flex;align-items:center;gap:7px;height:20px;white-space:nowrap}
  .contact-list svg{width:13px;height:13px;flex:none}
  .fb-mark{width:12px;height:12px;background:var(--sky);border-radius:2px;flex:none;margin-right:1px}

  /* partners */
  .partner{display:flex;align-items:center;gap:7px;font-family:"Crimson Pro",serif;white-space:nowrap}
  .partner-a{left:648px;top:1262px;font-size:20px;color:var(--navy)}
  .partner-a i{width:28px;height:28px;border:2px solid var(--navy);border-radius:50%;display:block;flex:none}
  .partner-b{left:842px;top:1260px;color:var(--partner-brown);font-size:13px;line-height:1.2}
  .partner-b i{width:14px;height:14px;background:var(--partner-green);display:block;flex:none}
  .partner-b small{display:block;font-size:9px;color:var(--partner-brown)}
</style>
</head>
<body>
<main class="poster">
  <svg class="backdrop" width="1018" height="1324" viewBox="0 0 1018 1324" aria-hidden="true">
    <defs>
      <linearGradient id="waveShade" x1="0" y1="0" x2="0.6" y2="0.4">
        <stop offset="0" stop-color="#b5b7d6"/>
        <stop offset=".45" stop-color="#3a4180"/>
        <stop offset="1" stop-color="#262e66"/>
      </linearGradient>
    </defs>
    <rect width="1018" height="1324" fill="var(--navy)"/>
    <rect width="1018" height="360" fill="var(--cream)"/>
    <path d="M0,180 C60,250 200,300 330,310 C560,318 760,270 880,275 C950,280 1000,320 1018,345 L1018,420 L0,420 Z" fill="var(--cyan)"/>
    <path d="M0,175 C50,250 180,305 300,318 C520,330 740,290 870,300 C950,308 1000,340 1018,360 L1018,430 L0,430 Z" fill="url(#waveShade)"/>
    <rect x="0" y="1229" width="1018" height="95" fill="var(--white)"/>
  </svg>

  <svg class="abs" style="left:856px;top:0" width="162" height="282" viewBox="0 0 162 282" role="img" aria-label="Faceted orange and amber low-poly corner decoration">
    <defs><linearGradient id="cornerGrad" x1="0" y1="0" x2="1" y2="1">
      <stop offset="0" stop-color="#f6c04a"/><stop offset=".55" stop-color="#ef8a2a"/><stop offset="1" stop-color="#8a3a1c"/>
    </linearGradient></defs>
    <path d="M0,0 L162,0 L162,282 L110,250 L80,120 Z" fill="url(#cornerGrad)"/>
  </svg>

  <svg class="abs" style="left:0;top:1170px" width="660" height="154" viewBox="0 0 660 154" role="img" aria-label="Faceted low-poly band in orange, teal and blue">
    <defs><linearGradient id="bandGrad" x1="0" y1="0" x2="1" y2="0">
      <stop offset="0" stop-color="#9c3a1e"/><stop offset=".3" stop-color="#f0922c"/><stop offset=".6" stop-color="#5cc3c9"/><stop offset="1" stop-color="#1f5fa8"/>
    </linearGradient></defs>
    <path d="M0,10 L120,45 L330,35 L520,60 L660,59 L610,154 L0,154 Z" fill="url(#bandGrad)"/>
  </svg>

  <div class="abs org-seal">Harborview Teen Circle of PL</div>
  <p class="abs edition">14th Annual Kindred Gathering &amp; Fair</p>
  <p class="abs tagline">TEENS EXPRESSING THEIR FAITH<br>THROUGH ART, MUSIC, AND DIALOGUE</p>
  <h1 class="abs event-title">INTERFAITH YOUTH FORUM</h1>
  <p class="abs theme"><span>THIS YEAR'S THEME:</span> “Who Are You?”</p>

  <p class="abs intro">All high school age faith groups are invited to come and join with 150 to 175 other high school students from various faith traditions to participate in the Harborview Teen Circle of Pine Lakes's Annual Kindred Voices Gathering. More than ever, our county and world need young leaders who are willing to learn from each other and build stronger communities!</p>
  <div class="abs divider-v" style="left:679px;top:399px;height:130px"></div>
  <div class="abs when">
    <p class="day">Sunday, <em>March 11<sup>th</sup>, 2018</em></p>
    <p class="time">11:00am-5:00pm</p>
    <p class="venue">Congregation Ner Adamah</p>
    <p class="addr">4187 W Larkmont Rd. Santa Ana, CA 92705</p>
  </div>

  <div class="abs strip">
    <div class="bars">
      <i style="width:375px;background:var(--sky)"></i>
      <i style="width:122px;background:#2d3670"></i>
      <i style="width:126px;background:var(--orange)"></i>
      <i style="width:123px;background:#f0d63a"></i>
      <i style="width:159px;background:#f6eab5"></i>
    </div>
    <div class="photos">
      <div style="width:375px;background:linear-gradient(180deg,#2a2220,#6b4a30 70%,#a8773f)" role="img" aria-label="Photo: students performing a dance on stage"></div>
      <div style="width:122px;background:linear-gradient(160deg,#3a3c4a,#8d6c56)" role="img" aria-label="Photo: hands working on a sand art piece"></div>
      <div style="width:126px;background:linear-gradient(180deg,#d9d2c8,#8a5a3a)" role="img" aria-label="Photo: teen playing drums"></div>
      <div style="width:282px;background:linear-gradient(160deg,#cfc6bd,#9a6a52 60%,#7b2a25)" role="img" aria-label="Photo: teens playing traditional string and keyboard instruments"></div>
    </div>
  </div>

  <h2 class="abs sec-title gathering-title">KINDRED <span>GATHERING</span></h2>
  <div class="abs rsvp gathering-rsvp">
    <small>RSVP for our KINDRED GATHERING</small>
    <strong>before February 18th, 2018</strong>
  </div>
  <div class="abs questions">
    <small>FORUM QUESTIONS</small>
    <b>at </b><a href="#">http://htcpl-example.org/home/kindred-fair/</a>
  </div>
  <div class="abs gathering-photo" style="background:linear-gradient(180deg,#b9a89a,#5a4a48 55%,#2c2a34)" role="img" aria-label="Photo: students seated together in a hall for discussion"></div>

  <div class="abs purpose">
    <p>The purpose of this Interfaith Youth Forum is to bring together young people from diverse ethnic, cultural, and religious backgrounds, and to engage them in dialogue. True dialogue is a conversation on a common subject between two or more persons of differing points of view and/or backgrounds. We feel that this commitment to dialogue will affect relationships in a constructive way in our places of worship and in our community.</p>
    <p class="clip">The forum itself involves having eight religiously diverse high school-age students, one adult, and youth leader around each table to discuss common questions. Our youth leaders act as facilitators, but it is stressed that it is the students we want to hear from.</p>
  </div>
  <div class="abs divider-h"></div>
  <div class="abs divider-v" style="left:616px;top:912px;height:317px"></div>

  <h2 class="abs sec-title festival-title">FAITH <span>FESTIVAL</span></h2>
  <p class="abs festival-text">The forum will include our Faith Festival portion of the program which families of the participants are welcomed to join. The Festival will include musical performances of all types from diverse religious communities. The differing performing arts include but are not limited to singing, dancing, instrumental music, storytelling, etc.</p>
  <div class="abs rsvp festival-rsvp">
    <small>RSVP for our FAITH FESTIVAL</small>
    <strong><b>by</b> February 11th, 2018<br><b>(Music, Song, Dance)</b></strong>
  </div>

  <h2 class="abs sec-title gallery-title">ART <span>GALLERY</span></h2>
  <p class="abs gallery-text">This event will include and Art Gallery display of students’ work, highlighting their expressions of faith, and artwork promoting learning, understanding, leadership, and service. Art includes any painting, illustration, sculpture, photography or other visual art.</p>
  <div class="abs gallery-due">
    <small>Art Work for our Art Gallery must be submitted</small>
    <strong>by <span>March 3rd, 2018</span></strong>
  </div>

  <p class="abs contact-label">Further<br>Information :</p>
  <ul class="abs contact-list">
    <li><svg viewBox="0 0 14 14" aria-hidden="true"><rect x="1" y="3" width="12" height="8" fill="none" stroke="#fff" stroke-width="1.2"/><path d="M1,3 L7,8 L13,3" fill="none" stroke="#fff" stroke-width="1.2"/></svg>htcplorg@mailbox-example.com</li>
    <li><svg viewBox="0 0 14 14" aria-hidden="true"><circle cx="7" cy="7" r="6" fill="none" stroke="#fff" stroke-width="1.1"/><ellipse cx="7" cy="7" rx="2.6" ry="6" fill="none" stroke="#fff" stroke-width="1"/><path d="M1,7 H13 M2,4 H12 M2,10 H12" stroke="#fff" stroke-width="1"/></svg>HTCPL-example.org</li>
    <li><span class="fb-mark"></span>Harborview Teen Circle of Pine Lakes</li>
  </ul>

  <div class="abs partner partner-a"><i></i>Brightpath Allies</div>
  <div class="abs partner partner-b"><i></i><span>Congregation Ner Adamah<small>www.CNAOC-example.com</small></span></div>
</main>
</body>
</html>
```